TIDAL VERGE needs bisness cards pronto

Bisness name is "TIDAL VERGE" new bisness the bisness includes lawn mowing, garden matanace, and any jobs around the house.
I need a card that is colorful and vibrant and the bisness of lawn mowing maybe with some nature with it. It also needs my contact details"Darren Quellby mobile 0413562049 call for free quote and email norma.vance@fernmail.com.au and a catchy tag line

Industry/Entity Type

House

Requirements
Must have
• Bisness name "TIDAL VERGE"
Contact details "0413562049"
Email norma.vance@fernmail.com.au
Call for free quote

```html
<!DOCTYPE html>
<html lang="en">
<head>
<meta charset="utf-8">
<title>Tidal Verge – Business Card</title>
<link rel="stylesheet" href="https://fonts.googleapis.com/css2?family=Open+Sans:wght@700;800&family=Oswald:wght@600;700&display=swap">
<style>
  :root {
    --stage: #2e2e2e;
    --card-border: #ffffff;
    --text-light: #ffffff;
    --title-shadow: #1d1d1d;
    --photo-top: #3d6b2c;
    --photo-bottom: #4fa82a;
  }
  * { margin: 0; padding: 0; box-sizing: border-box; }
  html, body {
    width: 1200px;
    height: 900px;
    overflow: hidden;
    background: var(--stage);
  }
  .business-card {
    position: absolute;
    left: 100px;
    top: 172px;
    width: 1000px;
    height: 556px;
    background: var(--card-border);
    padding: 34px;
  }
  .card-face {
    position: relative;
    width: 100%;
    height: 100%;
    overflow: hidden;
  }
  .garden-photo {
    position: absolute;
    inset: 0;
    background: linear-gradient(180deg, var(--photo-top) 0%, var(--photo-bottom) 100%);
  }
  .card-text {
    position: absolute;
    left: 38px;
    color: var(--text-light);
    line-height: 1;
    white-space: nowrap;
  }
  .phone {
    top: 24px;
    font-family: "Oswald", "Arial Narrow", sans-serif;
    font-weight: 700;
    font-size: 54px;
    letter-spacing: -0.5px;
    text-shadow: 2px 2px 2px rgba(0,0,0,0.45);
  }
  .quote-call {
    top: 90px;
    font-family: "Open Sans", Arial, sans-serif;
    font-weight: 700;
    font-size: 23px;
    text-shadow: 1px 1px 2px rgba(0,0,0,0.5);
  }
  .business-name {
    top: 168px;
    left: 30px;
    font-family: "Open Sans", Arial, sans-serif;
    font-weight: 800;
    font-size: 132px;
    letter-spacing: -2px;
    text-shadow: 5px 5px 0 var(--title-shadow);
  }
  .owner-name {
    top: 368px;
    font-family: "Oswald", "Arial Narrow", sans-serif;
    font-weight: 600;
    font-size: 54px;
    text-transform: uppercase;
    text-shadow: 2px 2px 2px rgba(0,0,0,0.35);
  }
  .email {
    top: 432px;
    font-family: "Open Sans", Arial, sans-serif;
    font-weight: 700;
    font-size: 23px;
    text-shadow: 1px 1px 2px rgba(0,0,0,0.4);
  }
</style>
</head>
<body>
  <div class="business-card">
    <div class="card-face">
      <div class="garden-photo" role="img" aria-label="Photo of a landscaped rock garden with grey limestone boulders, red foliage, green shrubs and a bright lawn"></div>
      <div class="card-text phone">0413562049</div>
      <div class="card-text quote-call">call for free quote</div>
      <div class="card-text business-name">Tidal Verge</div>
      <div class="card-text owner-name">Darren Quellby</div>
      <div class="card-text email">norma.vance@fernmail.com.au</div>
    </div>
  </div>
</body>
</html>
```